Book cover design for a collection of poetry - The Lanternfield

Book cover and back design need to be moody, nostalgic, reflective, ethereal. Melancholy and other worldly. Cover design should not be time specific to a period or place but if applicable should reflect British landscape. Book cover should be in tones of blue and must include the title and author (THE LANTERNFIELD BY CORWIN BLACKETT). We love the idea of rain, and looking out of a window. See attached designs. A world you are observing but not in.

Industry/Entity Type

Book Publisher

Font styles to use
Serif
Script

Colors
3176b5
3377b5
85acd3
eaf1f7
0792cd
33a6d7
86cae7
ecf7fb
86cfc6

Requirements
Must have
• The colour blue in it, must be melancholy and reflective.
Nice to have
• Rain in the cover.
Should not have
• Any bright colours.

```html
<!DOCTYPE html>
<html lang="en">
<head>
<meta charset="utf-8">
<title>The Lanternfield — Cover Wrap</title>
<link rel="stylesheet" href="https://fonts.googleapis.com/css2?family=Bodoni+Moda:opsz,wght@6..96,400;6..96,500;6..96,600&family=Playfair+Display:wght@400&display=swap">
<style>
  :root {
    --ink-deep: #0d1114;
    --back-grey: #3a3f42;
    --back-dark: #15191b;
    --spine-dark: #0f1315;
    --title-blue: #47a9d8;
    --title-blue-soft: #5ab6e0;
    --the-teal: #17323d;
    --author-pale: #b4d9ee;
    --blurb-white: #eef3f6;
    --glass-top: #b9c8cc;
    --glass-mid: #6f8a96;
    --glass-low: #3e5c4c;
  }
  html, body {
    margin: 0;
    padding: 0;
    width: 1200px;
    height: 910px;
    overflow: hidden;
    background: var(--ink-deep);
  }
  .cover-wrap {
    position: relative;
    width: 1200px;
    height: 910px;
    overflow: hidden;
  }

  /* Back cover */
  .back-cover {
    position: absolute;
    left: 0; top: 0;
    width: 636px; height: 910px;
  }
  .back-photo {
    position: absolute; inset: 0;
    background:
      radial-gradient(ellipse 60% 40% at 35% 30%, rgba(150,158,160,0.55), transparent 70%),
      radial-gradient(ellipse 50% 50% at 60% 75%, rgba(110,118,120,0.35), transparent 70%),
      linear-gradient(180deg, var(--back-grey) 0%, #2a2f31 45%, var(--back-dark) 100%);
  }
  .back-title {
    position: absolute;
    left: 0; top: 66px;
    width: 560px;
    text-align: center;
    color: var(--title-blue);
    font-family: "Bodoni Moda", "Playfair Display", serif;
    font-weight: 500;
  }
  .back-title .the {
    display: block;
    font-size: 25px;
    line-height: 30px;
  }
  .back-title .name {
    display: block;
    font-size: 38px;
    line-height: 46px;
    letter-spacing: 0.01em;
  }
  .blurb {
    position: absolute;
    left: 77px;
    width: 440px;
    margin: 0;
    color: var(--blurb-white);
    font-family: "Playfair Display", "Bodoni Moda", serif;
    font-size: 14px;
    line-height: 24.5px;
    letter-spacing: 0.28em;
    text-transform: uppercase;
  }
  .blurb-intro { top: 182px; }
  .blurb-close { top: 575px; }

  /* Spine */
  .spine {
    position: absolute;
    left: 570px; top: 0;
    width: 66px; height: 910px;
    background: linear-gradient(90deg, rgba(15,19,21,0) 0%, var(--spine-dark) 60%);
  }
  .spine-title, .spine-author {
    position: absolute;
    left: 33px;
    writing-mode: vertical-rl;
    transform: translateX(-50%);
    font-family: "Bodoni Moda", "Playfair Display", serif;
    white-space: nowrap;
  }
  .spine-title {
    top: 100px;
    color: var(--title-blue);
    font-size: 30px;
    font-weight: 500;
  }
  .spine-author {
    top: 528px;
    color: var(--author-pale);
    font-size: 24px;
    font-weight: 500;
    letter-spacing: 0.02em;
  }

  /* Front cover */
  .front-cover {
    position: absolute;
    left: 636px; top: 0;
    width: 564px; height: 910px;
    background: var(--ink-deep);
  }
  .front-photo {
    position: absolute;
    left: 40px; top: 0;
    width: 524px; height: 910px;
    background:
      linear-gradient(180deg, var(--glass-top) 0%, #93a8ae 25%, var(--glass-mid) 50%, #4f6e66 72%, var(--glass-low) 100%);
  }
  .front-the {
    position: absolute;
    left: 200px; top: 60px;
    color: var(--the-teal);
    font-family: "Bodoni Moda", "Playfair Display", serif;
    font-size: 80px;
    line-height: 90px;
    font-weight: 500;
    letter-spacing: -0.02em;
  }
  .front-title {
    position: absolute;
    left: 130px; top: 132px;
    width: 300px;
    margin: 0;
    color: var(--title-blue-soft);
    font-family: "Bodoni Moda", "Playfair Display", serif;
    font-weight: 500;
    text-align: center;
    opacity: 0.92;
  }
  .front-title span {
    display: block;
    font-size: 118px;
    line-height: 162px;
    letter-spacing: -0.03em;
    transform: scaleY(1.3);
  }
  .front-author {
    position: absolute;
    left: 140px; top: 780px;
    width: 300px;
    text-align: center;
    color: var(--author-pale);
    font-family: "Bodoni Moda", "Playfair Display", serif;
    font-weight: 500;
  }
  .front-author .first {
    display: block;
    font-size: 44px;
    line-height: 44px;
    letter-spacing: 0.16em;
  }
  .front-author .last {
    display: block;
    font-size: 44px;
    line-height: 42px;
    letter-spacing: -0.02em;
  }
</style>
</head>
<body>
<main class="cover-wrap">

  <section class="back-cover">
    <div class="back-photo" role="img" aria-label="Close-up of rain streaming down dark window glass in greys and black"></div>
    <h2 class="back-title">
      <span class="the">THE</span>
      <span class="name">LANTERNFIELD</span>
    </h2>
    <p class="blurb blurb-intro">The Lanternfield is a collection of poetry. Told in two parts we first meet Charles – aged, crippled and left alone in his inherited marsh house – reflecting on his life and his marriage to beautiful Alice who we meet in part two. Alice is suicidal, manically depressed and struggling with life as a wife and mother. She meets, harbors and falls in love with a soldier during WWII and her world is changed forever.</p>
    <p class="blurb blurb-close">Moving through the 20th century, this life and the next, The Lanternfield interweaves grief, loss, the after-life, mental illness, and ultimately the true nature of love.</p>
  </section>

  <section class="spine">
    <div class="spine-title">THE LANTERNFIELD</div>
    <div class="spine-author">CORWIN BLACKETT</div>
  </section>

  <section class="front-cover">
    <div class="front-photo" role="img" aria-label="View through a rain-covered paned window onto a misty grey sky and green British hillside"></div>
    <div class="front-the">THE</div>
    <h1 class="front-title">
      <span>LAN</span>
      <span>TER</span>
      <span>NFI</span>
      <span>ELD</span>
    </h1>
    <div class="front-author">
      <span class="first">CORWIN</span>
      <span class="last">BLACKETT</span>
    </div>
  </section>

</main>
</body>
</html>
```